DOUBLE SIDED BROCHURE NEEDED TO PROMOTE DOCTOR

I need a double sided DL size (99mm x 210mm) brochure, promoting a doctor seeing patients in a new area.

I want something professional. I have included the relevant information. I would also like the Dr's picture somwhere in the brochure, with a professional background. I wish to print these tomorrow, so i will pick a winner within 14 hours of posting this ad.

I have included an example of a brochures design that I recently saw, and its definietly a good starting point.

Medical

```html
<!DOCTYPE html>
<html lang="en">
<head>
<meta charset="utf-8">
<title>Dr. Haddad – Westhaven Clinic</title>
<link rel="stylesheet" href="https://fonts.googleapis.com/css2?family=Arimo:wght@400;700&family=Open+Sans:wght@400;600;700&display=swap">
<style>
  :root {
    --brand-blue: #2f8fe8;
    --label-blue: #3a8fe0;
    --accent-cyan: #4fd0f6;
    --corridor-pale: #e4fafd;
    --corridor-light: #b4eef8;
    --corridor-mid: #7ed8ec;
    --suit-dark: #1f2a36;
    --instrument-pale: #eef2fe;
    --instrument-blue: #b9c8fa;
    --ink: #1b1f26;
    --white: #ffffff;
  }
  * { margin: 0; padding: 0; box-sizing: border-box; }
  html, body { width: 1200px; height: 2550px; overflow: hidden; background: var(--white); }
  .brochure { position: relative; width: 1200px; height: 2550px; overflow: hidden; background: var(--white); color: var(--ink); font-family: "Open Sans", Arial, sans-serif; }

  .hero-photo {
    position: absolute; left: 0; top: 0; width: 1200px; height: 1216px;
    background:
      radial-gradient(ellipse 420px 620px at 1000px 1000px, rgba(31,42,54,0.85) 0%, rgba(31,42,54,0.55) 45%, rgba(31,42,54,0) 100%),
      radial-gradient(ellipse 260px 300px at 880px 420px, rgba(190,150,130,0.55) 0%, rgba(190,150,130,0) 100%),
      linear-gradient(180deg, var(--corridor-light) 0%, var(--corridor-pale) 35%, var(--corridor-light) 70%, var(--corridor-mid) 100%);
  }
  .hero-edge { position: absolute; left: 0; top: 0; width: 1200px; height: 80px; }

  .name-label {
    position: absolute; left: 0; top: 518px; width: 612px; height: 205px;
    background: var(--white); border-radius: 0 40px 40px 0;
    display: flex; align-items: center; justify-content: center;
  }
  .name-label h1 { font-family: "Arimo", Arial, sans-serif; font-weight: 700; font-size: 70px; color: var(--label-blue); }
  .name-tab { position: absolute; left: 0; top: 541px; width: 37px; height: 83px; background: var(--accent-cyan); }

  .instrument-illustration {
    position: absolute; left: 51px; top: 1250px; width: 384px; height: 260px; border-radius: 24px;
    background: linear-gradient(135deg, var(--instrument-pale) 0%, var(--instrument-blue) 100%);
  }
  .cross-icon { position: absolute; left: 1003px; top: 1422px; width: 136px; height: 136px; }
  .divider-band { position: absolute; left: 0; top: 1536px; width: 1200px; height: 20px; background: var(--brand-blue); }

  .letter { position: absolute; left: 61px; top: 1620px; width: 1076px; font-size: 34px; line-height: 50px; }
  .letter .greeting { margin-bottom: 52px; }
  .letter .para { text-align: justify; text-indent: 153px; margin-bottom: 22px; }

  .footer-shape { position: absolute; left: 0; top: 2117px; width: 1200px; height: 433px; }
  .referral { position: absolute; left: 60px; top: 2336px; }
  .referral .lead { font-size: 44px; line-height: 60px; }
  .referral .fax { font-size: 61px; line-height: 84px; }
  .clinic { position: absolute; right: 63px; top: 2243px; text-align: right; color: var(--white); }
  .clinic h2 { font-size: 41px; font-weight: 700; line-height: 60px; margin-bottom: 20px; }
  .clinic address { font-style: normal; font-size: 34px; line-height: 55px; }
</style>
</head>
<body>
<div class="brochure">
  <div class="hero-photo" role="img" aria-label="Photograph of Dr. Haddad in a dark jacket and checked shirt, seated in front of a bright blue hospital corridor"></div>
  <svg class="hero-edge" viewBox="0 0 1200 80" preserveAspectRatio="none" aria-hidden="true">
    <path d="M0 0 H1200 V60 L1160 75 L1120 58 L1080 72 L1040 56 L1000 70 L960 55 L920 68 L880 52 L840 66 L800 50 L760 64 L720 50 L680 62 L640 48 L600 62 L560 48 L520 64 L480 50 L440 66 L400 52 L360 68 L320 54 L280 70 L240 56 L200 72 L160 58 L120 74 L80 60 L40 76 L0 62 Z" fill="var(--accent-cyan)" opacity="0.55"/>
  </svg>
  <div class="name-label"><h1>Dr. Haddad</h1></div>
  <div class="name-tab"></div>

  <div class="instrument-illustration" role="img" aria-label="Illustration of a blue stethoscope"></div>
  <svg class="cross-icon" viewBox="0 0 136 136" aria-hidden="true">
    <circle cx="68" cy="68" r="66" fill="var(--label-blue)"/>
    <rect x="56" y="16" width="24" height="104" fill="var(--white)"/>
    <rect x="16" y="56" width="104" height="24" fill="var(--white)"/>
  </svg>
  <div class="divider-band"></div>

  <section class="letter">
    <p class="greeting">Dear Doctors,</p>
    <p class="para">We are pleased to announce that Dr. Samir Haddad is now consulting in Westhaven, seeing public and private patients.</p>
    <p class="para">Guaranteed appointment within two weeks, with patients having the option of surgery at Harbour Health Campus, Elmwood General Hospital or St. Aldric Private.</p>
  </section>

  <svg class="footer-shape" viewBox="0 0 1200 433" preserveAspectRatio="none" aria-hidden="true">
    <path d="M330 0 H1200 V433 H0 V230 C20 100 150 0 330 0 Z" fill="var(--accent-cyan)"/>
    <path d="M330 51 H1200 V433 H0 V225 C60 120 170 51 330 51 Z" fill="var(--brand-blue)"/>
  </svg>

  <div class="referral">
    <p class="lead">Please send all referrals by</p>
    <p class="fax">fax to (08) 5550 1234</p>
  </div>

  <div class="clinic">
    <h2>Westhaven Clinic</h2>
    <address>42 Kestrel Road<br>Westhaven WA 6999.<br>Phone: 1300 555 010</address>
  </div>
</div>
</body>
</html>
```